Need simple and modern looking business card with all my information on one side and logo on the other side
Info :
Company name - VELMAR CONSTRUCTION LLC
Company addres- 418 harbor 87th. Dunmoor park ny 10352
Email- velmarllc@tridomail.Com
Company phone number 555-318-6094
Cell number- 555-742-0583
Web site - velmarllc.Com
My name Gerald tomasino

Target Market(s)

Construction , home improvement, remodeling

Industry/Entity Type

Construction

Contact Information for Business Card

It has to be moder but at the same time simple

Font styles to use
Sans Serif

Colors
0255a3
ffffff
000000
f78f20
b1b1b1
9d9d9d
1b1b1b
33a6d7
ec1f27

Requirements
Must have
• My logo on one side maybe with a some kind of background on the other side all my information
Nice to have
• Some kind of background pictures provided by you .PLEASE HAVE ACCOUNT WITH PIXELVAULT WILL NOT PAY ANY EXTRA FEES .
Should not have
• Any kind of hamer, nails,screws, helmets itp. Please do not copy the other designs come up with something new.

```html
<!DOCTYPE html>
<html lang="en">
<head>
<meta charset="utf-8">
<title>Velmar Construction LLC — Business Card</title>
<link href="https://fonts.googleapis.com/css2?family=Open+Sans:wght@400;600;700&display=swap" rel="stylesheet">
<style>
  :root {
    --blue: #0255a3;
    --white: #ffffff;
    --black: #000000;
    --orange: #f78f20;
    --grey-light: #b1b1b1;
    --grey: #9d9d9d;
    --ink: #1b1b1b;
    --sky: #33a6d7;
    --red: #ec1f27;
    --backdrop: #e4e4e4;
  }
  * { margin: 0; padding: 0; box-sizing: border-box; }
  html, body {
    width: 1200px; height: 900px; overflow: hidden;
    background: var(--backdrop);
    font-family: "Open Sans", Arial, sans-serif;
  }
  .sheet {
    width: 1200px; height: 900px;
    display: flex; flex-direction: column;
    align-items: center; justify-content: center; gap: 60px;
  }
  .card {
    position: relative;
    width: 525px; height: 300px;
    background: var(--white);
    box-shadow: 0 2px 10px rgba(0,0,0,0.12);
    overflow: hidden;
  }

  .brand { display: flex; align-items: center; }
  .brand-mark { flex: none; background: var(--orange); }
  .brand-name {
    color: var(--ink); font-weight: 600; line-height: 1;
    text-transform: uppercase;
  }

  /* Front: name side */
  .card-front .brand {
    position: absolute; right: 34px; top: 122px; gap: 12px;
  }
  .card-front .brand-mark { width: 16px; height: 16px; }
  .card-front .brand-title { font-size: 50px; letter-spacing: 3px; }
  .card-front .brand-sub { font-size: 17px; letter-spacing: 2.4px; margin-top: 6px; }

  /* Back: info side */
  .card-back .brand {
    position: absolute; left: 34px; top: 170px; gap: 8px;
  }
  .card-back .brand-mark { width: 9px; height: 9px; }
  .card-back .brand-title { font-size: 24px; letter-spacing: 1.5px; }
  .card-back .brand-sub { font-size: 8.2px; letter-spacing: 1.1px; margin-top: 3px; }

  .contact {
    position: absolute; left: 290px; top: 40px;
    color: var(--ink); font-size: 12px; line-height: 1.3;
  }
  .contact-name {
    color: var(--orange); font-weight: 700; font-size: 13px;
    margin-bottom: 26px;
  }
  .contact-row { display: flex; align-items: flex-start; gap: 7px; }
  .contact-row + .contact-row { margin-top: 2px; }
  .contact-row.address { margin-bottom: 14px; }
  .icon { width: 12px; height: 12px; flex: none; margin-top: 2px; }
</style>
</head>
<body>
<main class="sheet">

  <section class="card card-front" aria-label="Card front">
    <div class="brand">
      <span class="brand-mark"></span>
      <div class="brand-name">
        <div class="brand-title">Velmar</div>
        <div class="brand-sub">Construction LLC</div>
      </div>
    </div>
  </section>

  <section class="card card-back" aria-label="Card back">
    <div class="brand">
      <span class="brand-mark"></span>
      <div class="brand-name">
        <div class="brand-title">Velmar</div>
        <div class="brand-sub">Construction LLC</div>
      </div>
    </div>

    <div class="contact">
      <div class="contact-name">Gerald tomasino</div>

      <div class="contact-row address">
        <svg class="icon" viewBox="0 0 12 12" aria-hidden="true">
          <circle cx="6" cy="6" r="6" fill="var(--sky)"/>
          <path d="M6 2.6a2 2 0 0 0-2 2c0 1.5 2 4 2 4s2-2.5 2-4a2 2 0 0 0-2-2z" fill="var(--white)"/>
        </svg>
        <span>418 harbor 87th.<br>Dunmoor park ny 10352</span>
      </div>

      <div class="contact-row">
        <svg class="icon" viewBox="0 0 12 12" aria-hidden="true">
          <circle cx="6" cy="6" r="6" fill="var(--red)"/>
          <path d="M4 3.2l1.2 1.4-.6.8a4 4 0 0 0 2 2l.8-.6L8.8 8 8 8.8C6 8.6 3.4 6 3.2 4z" fill="var(--white)"/>
        </svg>
        <span>555-742-0583</span>
      </div>
      <div class="contact-row">
        <svg class="icon" viewBox="0 0 12 12" aria-hidden="true">
          <circle cx="6" cy="6" r="6" fill="var(--grey)"/>
          <rect x="4.2" y="2.8" width="3.6" height="6.4" rx="0.6" fill="var(--white)"/>
        </svg>
        <span>555-318-6094</span>
      </div>
      <div class="contact-row">
        <svg class="icon" viewBox="0 0 12 12" aria-hidden="true">
          <circle cx="6" cy="6" r="6" fill="var(--orange)"/>
          <rect x="3" y="4" width="6" height="4.2" fill="var(--white)"/>
          <path d="M3 4l3 2.3L9 4" fill="none" stroke="var(--orange)" stroke-width="0.7"/>
        </svg>
        <span>velmarllc@tridomail.Com</span>
      </div>
      <div class="contact-row">
        <svg class="icon" viewBox="0 0 12 12" aria-hidden="true">
          <circle cx="6" cy="6" r="6" fill="var(--ink)"/>
          <circle cx="6" cy="6" r="3" fill="none" stroke="var(--white)" stroke-width="0.8"/>
          <path d="M3 6h6M6 3v6" stroke="var(--white)" stroke-width="0.6"/>
        </svg>
        <span>velmarllc.Com</span>
      </div>
    </div>
  </section>

</main>
</body>
</html>
```